Business Card Design Project

Bold, modern, clean business card design needed. Prefer double sided with art logo on the back. Front of card with company name logo, no art.

Target Market(s)

Our consulting company supports local, state and federal law enforcement officers. Therefore the design should be clean and direct with no flash or arrogance to it.

Industry/Entity Type

Business

```html
<!DOCTYPE html>
<html lang="en">
<head>
<meta charset="utf-8">
<title>Kestrel Technologies – Business Cards</title>
<link href="https://fonts.googleapis.com/css2?family=Arimo:wght@400;700&family=Michroma&display=swap" rel="stylesheet">
<style>
  :root {
    --bg: #2a2a2a;
    --card-white: #f6f6f6;
    --brand-green: #8cbf12;
    --brand-green-dark: #7aab0c;
    --ink: #1c1c1c;
    --ink-soft: #3a3a3a;
    --on-green: #ffffff;
  }
  * { box-sizing: border-box; margin: 0; padding: 0; }
  html, body {
    width: 1200px; height: 997px; overflow: hidden;
    background: var(--bg);
    font-family: "Arimo", Arial, sans-serif;
  }
  .canvas { position: relative; width: 1200px; height: 997px; }

  .card {
    position: absolute; left: 300px;
    width: 600px; height: 340px;
    border-radius: 26px; overflow: hidden;
    background: var(--card-white);
  }
  .card--back { top: 110px; }
  .card--front { top: 540px; }

  /* Brand lockup: plain circle + name */
  .brand { display: flex; flex-direction: column; align-items: center; }
  .brand__mark {
    width: 64px; height: 64px; border-radius: 50%;
    background: var(--brand-green); margin-bottom: 14px;
  }
  .brand__name {
    font-family: "Michroma", "Arimo", sans-serif;
    color: var(--ink-soft); text-align: center; line-height: 1.25;
    font-size: 30px; letter-spacing: 1px;
  }
  .brand__name small { display: block; font-size: 13px; letter-spacing: 6px; }

  /* Back card */
  .card--back .brand { position: absolute; top: 46px; left: 0; right: 0; }
  .slogan-band {
    position: absolute; left: 0; right: 0; bottom: 0; height: 104px;
    background:
      linear-gradient(to bottom,
        var(--brand-green) 0 4px, var(--card-white) 4px 9px,
        var(--brand-green) 9px 13px, var(--card-white) 13px 18px,
        var(--brand-green) 18px 100%);
  }
  .slogan-band__text {
    position: absolute; left: 0; right: 0; top: 50px;
    text-align: center; color: var(--on-green);
    font-size: 15px; letter-spacing: 4px;
  }

  /* Front card */
  .card--front .brand {
    position: absolute; left: 0; width: 290px; top: 92px;
  }
  .card--front .brand__name { font-size: 24px; }
  .card--front .brand__name small { font-size: 11px; letter-spacing: 4px; }
  .contact-panel {
    position: absolute; top: 0; bottom: 0; left: 300px; right: 0;
    background:
      linear-gradient(to right,
        var(--brand-green) 0 4px, var(--card-white) 4px 9px,
        var(--brand-green) 9px 13px, var(--card-white) 13px 18px,
        var(--brand-green) 18px 100%);
  }
  .person { position: absolute; left: 52px; top: 34px; }
  .person__name { font-weight: 700; font-size: 19px; color: var(--ink); }
  .person__role { font-size: 12px; color: var(--on-green); margin-left: 26px; margin-top: 2px; }
  .contact-list { position: absolute; left: 46px; top: 146px; list-style: none; }
  .contact-list li {
    display: flex; align-items: flex-start; gap: 8px;
    color: var(--on-green); font-size: 14px; line-height: 1.2;
    margin-bottom: 10px;
  }
  .contact-list svg { flex: none; width: 20px; height: 20px; }
</style>
</head>
<body>
<main class="canvas">

  <section class="card card--back" aria-label="Card back">
    <div class="brand">
      <span class="brand__mark"></span>
      <p class="brand__name">KESTREL<small>TECHNOLOGIES</small></p>
    </div>
    <div class="slogan-band">
      <p class="slogan-band__text">YOUR SLOGAN / TAGLINE HERE</p>
    </div>
  </section>

  <section class="card card--front" aria-label="Card front">
    <div class="brand">
      <span class="brand__mark"></span>
      <p class="brand__name">KESTREL<small>TECHNOLOGIES</small></p>
    </div>
    <div class="contact-panel">
      <div class="person">
        <p class="person__name">YOUR NAME</p>
        <p class="person__role">Centre Director</p>
      </div>
      <ul class="contact-list">
        <li>
          <svg viewBox="0 0 20 20" aria-hidden="true"><circle cx="10" cy="10" r="10" fill="#fff"/><path d="M6 7c0-1 1-2 2-2l1 2-1 1c1 2 2 3 4 4l1-1 2 1c0 1-1 2-2 2-4 0-7-3-7-7z" fill="#7aab0c"/></svg>
          <span>+39 300 5550147</span>
        </li>
        <li>
          <svg viewBox="0 0 20 20" aria-hidden="true"><circle cx="10" cy="10" r="10" fill="#fff"/><rect x="7" y="5" width="6" height="3" fill="#7aab0c"/><rect x="5" y="8" width="10" height="5" rx="1" fill="#7aab0c"/><rect x="7" y="12" width="6" height="3" fill="#7aab0c"/></svg>
          <span>(+123) 456 7890</span>
        </li>
        <li>
          <svg viewBox="0 0 20 20" aria-hidden="true"><circle cx="10" cy="10" r="10" fill="#fff"/><rect x="5" y="6.5" width="10" height="7" fill="#7aab0c"/><path d="M5 6.5l5 4 5-4" fill="none" stroke="#fff" stroke-width="1"/></svg>
          <span>info@northgatefinancial.com</span>
        </li>
        <li>
          <svg viewBox="0 0 20 20" aria-hidden="true"><circle cx="10" cy="10" r="10" fill="#fff"/><path d="M10 4a4 4 0 0 1 4 4c0 3-4 8-4 8s-4-5-4-8a4 4 0 0 1 4-4z" fill="#7aab0c"/><circle cx="10" cy="8" r="1.5" fill="#fff"/></svg>
          <span>Via Aurora,<br>30 62010 Castelverde (MC), Italy</span>
        </li>
      </ul>
    </div>
  </section>

</main>
</body>
</html>
```